New Business Card Design for Business Consulting Business

We need a business card design that reflects the simplicity of our business. We partner with our clients to help them deliver change. We are a different kind of business consulting group. We don't just provide you with the theory. We provide you with the leadership and capability to execute change.

Vonduro is a professional services organisation that partners with their clients to lead the execution of strategic process and system improvement initiatives. Vonduro combines hands on delivery with coaching in best practice methodologies and approaches to build their clients capabilities to ensure their ongoing success in project implementations. Vonduro offers business advisory services in Project Management, Business Process Management, Change Management and Business Analytics.

Reason: Hi Designers, Thanks for all of your great designs. There are some really creative and cool ideas. Everyone is really capturing the essence of my business Vonduro. I am extending the deadline for the business card design by 6 days as I need to consult my Marketing colleague who won't be back in Australia until Wednesday. I would like to sit down with them and review all of the best designs. The key themes of the things I have really liked on my first review are: 1) Capturing the company website on the back of the card. 2) Including the company logo on the back of the card too. 3) Including the types of services on the back of the card that the company offers - Project Management - Business Process Management - Change Management - Business Analytics 4) Utilising some images on the back of the card Just so everyone knows the colour palette for the Vonduro company logo is: R: 0 G: 86 B: 162 or C: 97% M: 73% Y: 4% K: 0% Thanks Gareth

Hi Designers,

Thanks for all of your submissions to date.  I am working through each design and will provide feedback on all the great work.

One thing I would like to ask is if you could submit a version that has my academic credentials under or after my name.  I am not a big fan of doing this but as I am in business consulting it does seem to be quite common.

I hold a Bachelor of Commerce (BCom) and a Master of Business Administration (MBA)

Thanks

Gareth

Hi Designers,

Thanks for all of your fantastic designs.  There are some really great designs here for my business.  I am still in the process of reviewing designs and should have this completed by tomorrow.  Some of the things I have learnt from this round of designs are:

1) I prefer to have the card without my academic qualifications

2) I really like cards that have a blue back

3) I prefer to have my name and title either left or right of centre

I hope this helps and I will endeavour to get through all of the designs tomorrow

Cheers

Gareth

Target Market(s)

We target large corporate organisations

Industry/Entity Type

Leadership

Requirements
Must have
• Must have the following business details

Gareth Pilling - Director
Address: Level 7, 82 Harlow Street, Melbourne, Australia, 3000
Phone: +61 3 527 840 213
Fax: +61 3 9214 5037
Email: gareth.pilling@vonduro-example.com.au
LinkedIn: au.linkedin.com/in/garethjpilling/
Twiiter: @garethjpilling
Website: www.vonduro-example.com.au

```html
<!DOCTYPE html>
<html lang="en">
<head>
<meta charset="utf-8">
<title>Vonduro Business Card</title>
<link rel="stylesheet" href="https://fonts.googleapis.com/css2?family=Open+Sans:wght@400;600;700&display=swap">
<style>
  :root {
    --brand-blue: #0056a2;
    --brand-blue-dark: #0a3f78;
    --brand-blue-light: #2a7cc7;
    --paper: #ffffff;
    --ink: #1d2b3a;
    --muted: #6b7785;
    --stage: #e9ebee;
  }
  * { box-sizing: border-box; margin: 0; padding: 0; }
  html, body { width: 720px; height: 1200px; overflow: hidden; }
  body {
    background: var(--stage);
    font-family: "Open Sans", Arial, sans-serif;
    display: flex;
    flex-direction: column;
    align-items: center;
    justify-content: center;
    gap: 90px;
  }
  .card {
    width: 640px;
    height: 390px;
    border-radius: 22px;
    overflow: hidden;
    position: relative;
    box-shadow: 0 6px 20px rgba(0, 0, 0, 0.15);
  }

  /* Front */
  .card-front { background: var(--paper); display: flex; flex-direction: column; }
  .front-head {
    height: 200px;
    display: flex;
    align-items: center;
    justify-content: space-between;
    padding: 0 44px;
  }
  .wordmark {
    display: flex;
    align-items: center;
    gap: 10px;
    color: var(--brand-blue);
    font-weight: 600;
    font-size: 44px;
    letter-spacing: -0.5px;
  }
  .wordmark-dot {
    width: 26px; height: 26px; border-radius: 50%;
    background: var(--brand-blue);
  }
  .person { text-align: left; border-left: 2px solid var(--brand-blue); padding-left: 18px; }
  .person-name { color: var(--brand-blue); font-weight: 700; font-size: 26px; }
  .person-title { color: var(--muted); font-size: 15px; margin-top: 4px; letter-spacing: 1px; }

  .front-band {
    flex: 1;
    background: var(--brand-blue);
    border-top: 6px solid var(--brand-blue-light);
    color: var(--paper);
    padding: 22px 44px 18px;
    display: flex;
    flex-direction: column;
    justify-content: space-between;
  }
  .contact-grid { display: grid; grid-template-columns: 1.25fr 1fr; gap: 10px 24px; }
  .contact-line { display: flex; align-items: center; gap: 10px; font-size: 13px; white-space: nowrap; }
  .contact-line svg { width: 18px; height: 18px; flex: none; }
  .social-mark { width: 18px; height: 18px; border-radius: 50%; background: var(--paper); flex: none; }
  .address { border-top: 1px solid rgba(255, 255, 255, 0.35); padding-top: 10px; }

  /* Back */
  .card-back {
    background: var(--brand-blue);
    color: var(--paper);
    display: flex;
    flex-direction: column;
    align-items: center;
    justify-content: center;
  }
  .card-back .wordmark { color: var(--paper); font-size: 78px; }
  .card-back .wordmark-dot { width: 44px; height: 44px; background: var(--paper); }
  .company-suffix { font-size: 14px; letter-spacing: 6px; margin-top: 2px; align-self: center; padding-left: 160px; }
  .website { margin-top: 34px; font-size: 18px; letter-spacing: 7px; text-transform: uppercase; }
  .back-stripe {
    position: absolute; left: 0; right: 0; bottom: 0; height: 46px;
    background: var(--brand-blue-dark);
  }
</style>
</head>
<body>

<article class="card card-front">
  <header class="front-head">
    <div class="wordmark"><span class="wordmark-dot"></span>Vonduro</div>
    <div class="person">
      <p class="person-name">Gareth Pilling</p>
      <p class="person-title">Director</p>
    </div>
  </header>
  <section class="front-band">
    <div class="contact-grid">
      <p class="contact-line"><span class="social-mark"></span>@garethjpilling</p>
      <p class="contact-line">
        <svg viewBox="0 0 24 24" fill="#fff"><path d="M6.6 10.8a15.1 15.1 0 0 0 6.6 6.6l2.2-2.2a1 1 0 0 1 1-.25 11.4 11.4 0 0 0 3.6.57 1 1 0 0 1 1 1V20a1 1 0 0 1-1 1A17 17 0 0 1 3 4a1 1 0 0 1 1-1h3.5a1 1 0 0 1 1 1c0 1.25.2 2.45.57 3.57a1 1 0 0 1-.25 1z"/></svg>
        +61 3 527 840 213
      </p>
      <p class="contact-line"><span class="social-mark"></span>au.linkedin.com/in/garethjpilling/</p>
      <p class="contact-line">
        <svg viewBox="0 0 24 24" fill="#fff"><path d="M7 3h10v5H7zM4 9h16a1 1 0 0 1 1 1v7h-4v4H7v-4H3v-7a1 1 0 0 1 1-1zm5 7v3h6v-3z"/></svg>
        +61 3 9214 5037
      </p>
      <p class="contact-line">
        <svg viewBox="0 0 24 24" fill="#fff"><path d="M3 5h18v14H3zm2 2v.4l7 4.6 7-4.6V7zm0 2.8V17h14V9.8l-7 4.6z"/></svg>
        gareth.pilling@vonduro-example.com.au
      </p>
    </div>
    <p class="contact-line address">
      <svg viewBox="0 0 24 24" fill="#fff"><path d="M12 2a7 7 0 0 0-7 7c0 5.2 7 13 7 13s7-7.8 7-13a7 7 0 0 0-7-7zm0 9.5A2.5 2.5 0 1 1 12 6.5a2.5 2.5 0 0 1 0 5z"/></svg>
      Level 7, 82 Harlow Street, Melbourne, Australia, 3000
    </p>
  </section>
</article>

<article class="card card-back">
  <div class="wordmark"><span class="wordmark-dot"></span>Vonduro</div>
  <p class="company-suffix">PTY LTD</p>
  <p class="website">www.vonduro-example.com.au</p>
  <div class="back-stripe"></div>
</article>

</body>
</html>
```